exclusive Speakeasy Bar Web design in New Jersey USA

We are opening a speakeasy in New Jersey USA soon. we are looking for a web designer to do our web site including the coding. we a looking for a 4 to 5 page web design. the site will be mostly static. home page, contact page, menu page and a link to a 3rd party site (most likely Qelmo) for reservations. we are looking for this designer to do our menu deign as well. we are looking for a quick turnaround 7-10 days. i am attaching some pictures for the designers to see the concept design and the actual current pictures with our logo as well. professionally taken pictures will be provided later on. our photographer will be taking the pictures in the next week.

Industry/Entity Type

Restaurant, Bar, Speakeasy

Coding

Coded - Design and coding required

Number of Pages Required

4 page

Requirements
Must have
• home page, contact page, menu page and a link to qelmo.com for reservations
Nice to have
• some videos

```html
<!DOCTYPE html>
<html lang="en">
<head>
<meta charset="utf-8">
<title>Lantern Nine — New Jersey Speakeasy</title>
<link href="https://fonts.googleapis.com/css2?family=Tinos:wght@400;700&family=Great+Vibes&family=Poppins:wght@400;500;600&display=swap" rel="stylesheet">
<style>
:root{
  --bg:#0c161b;
  --bg-deep:#050708;
  --bg-foot:#0d1519;
  --gold:#b5853a;
  --white:#ffffff;
  --ink:#1a1a1a;
  --line:rgba(200,190,170,.45);
  --field:#d9d9d9;
}
*{box-sizing:border-box;margin:0;padding:0}
html,body{width:1200px;height:2700px;overflow:hidden;background:var(--bg);color:var(--white);font-family:"Poppins",sans-serif}
a{color:inherit;text-decoration:none}
.page{position:relative;width:1200px;height:2700px}
.guide{position:absolute;top:0;width:1px;height:2628px;background:var(--line);z-index:5}
.guide.left{left:110px}.guide.right{left:1089px}

.hero{position:absolute;left:0;top:0;width:1200px;height:640px;
  background:
    radial-gradient(ellipse 260px 120px at 380px 215px,rgba(240,215,170,.35),transparent 70%),
    radial-gradient(ellipse 300px 130px at 690px 210px,rgba(240,215,170,.35),transparent 70%),
    radial-gradient(ellipse 420px 200px at 760px 300px,rgba(110,170,175,.45),transparent 70%),
    radial-gradient(ellipse 300px 180px at 1120px 300px,rgba(110,170,175,.35),transparent 70%),
    radial-gradient(ellipse 260px 160px at 160px 560px,rgba(200,130,50,.75),transparent 70%),
    radial-gradient(ellipse 200px 140px at 560px 600px,rgba(200,130,50,.6),transparent 70%),
    radial-gradient(ellipse 220px 130px at 1100px 610px,rgba(200,130,50,.55),transparent 70%),
    radial-gradient(ellipse 520px 160px at 760px 440px,rgba(60,50,60,.9),transparent 75%),
    linear-gradient(180deg,#1b2226 0%,#27353a 40%,#2b2a2c 70%,#4a3a2c 100%);}
.header{position:absolute;left:0;top:0;width:1200px;height:100px;background:rgba(12,20,24,.85);z-index:3}
.brand{position:absolute;left:30px;top:26px;width:54px;font-family:"Tinos",serif;font-size:11px;color:var(--white);text-align:center;line-height:1.25}
.nav a{position:absolute;top:45px;color:var(--white);font-size:9.5px;font-weight:600;letter-spacing:.2px}
.nav a.active::after{content:"";position:absolute;left:-6px;right:-6px;top:19px;height:1px;background:var(--white)}
.book{position:absolute;right:28px;top:39px;width:56px;height:23px;background:var(--gold);color:var(--ink);font-family:"Tinos",serif;font-weight:700;font-size:11px;letter-spacing:1.5px;display:flex;align-items:center;justify-content:center}
.hero-title{position:absolute;left:141px;top:260px;font-family:"Tinos",serif;font-weight:700;font-size:56px;line-height:58px;z-index:2}

.intro{position:absolute;top:700px;left:0;width:1200px;text-align:center}
.intro h2{font-family:"Tinos",serif;font-weight:700;font-size:35px;line-height:44px}
.intro .script{font-family:"Great Vibes",cursive;color:var(--gold);font-size:34px;line-height:40px}
.intro p{width:612px;margin:18px auto 0;font-size:10px;line-height:24px;font-weight:500}

.gallery{position:absolute;left:111px;top:981px;display:grid;grid-template-columns:repeat(3,315px);grid-auto-rows:320px;gap:16px 17px}
.photo{width:315px;height:320px}
.photo.shelves{background:
  radial-gradient(ellipse 120px 60px at 200px 80px,rgba(240,200,120,.45),transparent 70%),
  linear-gradient(90deg,#3b2a1e 0,#2a1c14 14%,#8a4e2a 30%,#b8732e 55%,#7a3a24 80%,#3a281c 100%);}
.photo.bar{background:
  radial-gradient(ellipse 140px 40px at 200px 110px,rgba(240,230,210,.45),transparent 70%),
  radial-gradient(ellipse 160px 90px at 110px 180px,rgba(200,130,50,.6),transparent 70%),
  linear-gradient(160deg,#1c2226 0%,#2e3538 40%,#8a5a40 62%,#3c6a66 85%,#1e2a2c 100%);}
.photo.lounge{background:
  radial-gradient(ellipse 180px 90px at 220px 210px,rgba(210,140,50,.85),transparent 70%),
  radial-gradient(ellipse 110px 70px at 60px 150px,rgba(20,20,22,.9),transparent 70%),
  linear-gradient(180deg,#1f2620 0%,#2f3a30 35%,#4a4a38 60%,#6a4c34 100%);}

.mark{position:absolute;left:0;top:1820px;width:1200px;display:flex;justify-content:center;align-items:center;gap:14px;font-family:"Tinos",serif;font-size:40px;color:var(--white)}
.mark i{display:block;width:14px;height:14px;background:var(--gold)}
.cta{position:absolute;left:470px;top:2008px;width:260px;height:60px;background:var(--gold);color:var(--white);font-family:"Tinos",serif;font-size:14px;display:flex;align-items:center;justify-content:center}

.contact{position:absolute;left:0;top:2150px;width:1200px;height:478px;background:var(--bg-deep)}
.contact h3{position:absolute;left:141px;top:50px;font-family:"Tinos",serif;font-weight:400;font-size:30px}
.contact .lead{position:absolute;left:141px;top:98px;width:365px;font-size:10px;line-height:24px;font-weight:500}
.info{position:absolute;left:141px;display:flex;font-size:10px;font-weight:500;line-height:24px}
.info svg{width:16px;height:16px;margin-top:4px;margin-right:48px}
.field{position:absolute;left:585px;width:475px;border:1px solid var(--field);font-size:10px;font-weight:500;padding:14px 29px;color:var(--white)}
.submit{position:absolute;left:585px;top:378px;width:125px;height:50px;background:var(--gold);font-family:"Tinos",serif;font-weight:700;font-size:14px;display:flex;align-items:center;justify-content:center}

.footer{position:absolute;left:0;top:2628px;width:1200px;height:72px;background:var(--bg-foot)}
.footer .book{left:141px;right:auto;top:25px}
.footer .copy{position:absolute;left:0;width:1200px;top:28px;text-align:center;font-size:10px;font-weight:500}
.social{position:absolute;right:134px;top:27px;display:flex;gap:18px;font-size:11px;font-weight:600;color:var(--gold)}
</style>
</head>
<body>
<div class="page">
  <div class="hero" role="img" aria-label="Photo of the lounge interior with velvet booths, globe chandeliers and amber leather chairs"></div>
  <header class="header">
    <div class="brand">Lantern<br>Nine</div>
    <nav class="nav">
      <a class="active" href="#" style="left:418px">HOME</a>
      <a href="#" style="left:486px">ABOUT</a>
      <a href="#" style="left:558px">MENU</a>
      <a href="#" style="left:626px">RESERVATION</a>
      <a href="#" style="left:733px">CONTACT</a>
    </nav>
    <a class="book" href="#">QELMO</a>
  </header>
  <h1 class="hero-title">New Jersey Best<br>Speakeasy</h1>

  <section class="intro">
    <h2>Introducing The Best Speakeasy in</h2>
    <div class="script">New Jersey</div>
    <p>Lorem ipsum dolor sit amet, consectetur adipiscing elit, sed do eiusmod tempor incididunt ut labore et dolore magna aliqua. Aliquet lectus proin nibh nisl condimentum id venenatis a. Magnis dis parturient montes nascetur ridiculus. Nunc id cursus metus aliquam eleifend. Nulla aliquet enim tortor at auctor urna. Duis at consectetur lorem donec massa. Parturient montes nascetur ridiculus mus. In massa tempor nec feugiat.</p>
  </section>

  <div class="gallery">
    <div class="photo shelves" role="img" aria-label="Photo of backlit liquor shelves"></div>
    <div class="photo bar" role="img" aria-label="Photo of the bar counter and seating"></div>
    <div class="photo lounge" role="img" aria-label="Photo of mural wall with tufted chairs"></div>
    <div class="photo shelves" role="img" aria-label="Photo of backlit liquor shelves"></div>
    <div class="photo bar" role="img" aria-label="Photo of the bar counter and seating"></div>
    <div class="photo lounge" role="img" aria-label="Photo of mural wall with tufted chairs"></div>
  </div>

  <div class="mark"><i></i>Lantern Nine</div>
  <a class="cta" href="#">Make Reservation</a>

  <section class="contact">
    <h3>Contact Us</h3>
    <p class="lead">Lorem ipsum dolor sit amet, consectetur adipiscing elit, sed do eiusmod tempor incididunt ut labore et dolore magna aliqua. Aliquet lectus proin nibh nisl condimentum id venenatis a. Magnis dis parturient montes nascetur ridiculus.</p>
    <div class="info" style="top:214px">
      <svg viewBox="0 0 16 16"><path fill="#b5853a" d="M3 1l3 3-1.5 2a9 9 0 0 0 5.5 5.5L12 10l3 3-2 2C7 15 1 9 1 3z"/></svg>+555 014 2368</div>
    <div class="info" style="top:256px">
      <svg viewBox="0 0 16 16"><path fill="#b5853a" d="M1 3h14v10H1z"/><path fill="none" stroke="#050708" stroke-width="1.4" d="M1 3l7 6 7-6"/></svg>hello@lanternnine.com</div>
    <div class="info" style="top:298px">
      <svg viewBox="0 0 16 16"><path fill="#b5853a" d="M8 0a5.5 5.5 0 0 0-5.5 5.5C2.5 10 8 16 8 16s5.5-6 5.5-10.5A5.5 5.5 0 0 0 8 0zm0 7.5a2 2 0 1 1 0-4 2 2 0 0 1 0 4z"/></svg><span>48 Elm Row Newjersey<br>Lantern Nine</span></div>
    <div class="field" style="top:58px;height:50px">Enter Name</div>
    <div class="field" style="top:138px;height:50px">Enter Email</div>
    <div class="field" style="top:218px;height:130px">Type Your Message Here</div>
    <div class="submit">Submit</div>
  </section>

  <footer class="footer">
    <a class="book" href="#">QELMO</a>
    <div class="copy">All Rights Reserved Lantern Nine © 2023</div>
    <div class="social"><span>Vistly</span><span>Murmr</span><span>Circlo</span></div>
  </footer>

  <div class="guide left"></div>
  <div class="guide right"></div>
</div>
</body>
</html>
```